Site for small consultancy for think tanks and non-profits

Small website to advertise consultancy. Description of services, copy about values, host page for podcast, contact details/email subscription, endorsements. Already have logo and two "house" colours. I need to be able to manage posting things on the website myself. Emphasis is on good quality advice and services, but at a value for money cost.

Target Market(s)

Market is global, but especially in emerging countries.

Industry/Entity Type

Non-Profit

Coding

Coded - Design and coding required

Number of Pages Required

5+ page

Font styles to use
Other font styles liked:
• Nordique Pro

Requirements
Must have
• Logo, and suitable use of the logo colours
Nice to have
• I'm not sure if the logo font is suitable for the whole website, but it should be featured in key areas.

```html
<!DOCTYPE html>
<html lang="en">
<head>
<meta charset="utf-8">
<title>Kelvo – Think Tanks &amp; Non-Profits</title>
<link href="https://fonts.googleapis.com/css2?family=Open+Sans:wght@400;600;700;800&display=swap" rel="stylesheet">
<style>
  :root{
    --purple:#4a2466;
    --purple-deep:#42215c;
    --coral:#f5564a;
    --slate:#4a4a4a;
    --lavender:#f6effd;
    --ink:#1d1d1d;
    --white:#ffffff;
    --footer:#2e3134;
    --footer-base:#242729;
    --footer-line:#3d4044;
    --muted:#b9bcc0;
  }
  *{box-sizing:border-box;margin:0;padding:0}
  html,body{width:1200px;height:2625px;overflow:hidden}
  body{font-family:"Open Sans",Arial,sans-serif;color:var(--ink);position:relative;background:var(--white)}
  .abs{position:absolute}
  ul{list-style:none}

  /* Hero */
  .hero{left:0;top:0;width:1200px;height:538px;background:radial-gradient(ellipse at 75% 45%,#3b78ad 0%,#1f5488 35%,#123a66 70%,#0d2c52 100%)}
  .topbar{left:0;top:0;width:1200px;height:44px;background:rgba(40,52,66,.55);color:var(--white);font-size:12px;font-weight:600}
  .topbar .contact{left:235px;top:14px;display:flex;gap:30px;align-items:center}
  .topbar .contact span{display:flex;gap:8px;align-items:center}
  .topbar .socials{left:863px;top:15px;display:flex;gap:18px}
  .topbar .socials i{width:13px;height:13px;border-radius:50%;background:var(--white);display:block;opacity:.9}
  .brand{left:235px;top:57px;height:75px;display:flex;align-items:center;gap:12px;color:var(--white);font-size:44px;font-weight:400;letter-spacing:-1px}
  .brand .mark{width:14px;height:14px;background:var(--coral)}
  .nav{left:606px;top:87px;display:flex;gap:29px;font-size:12px;font-weight:700;color:var(--white)}
  .hero-copy{left:0;top:182px;width:1200px;text-align:center;color:var(--white)}
  .hero-copy h1{font-size:45px;font-weight:700;letter-spacing:.2px;line-height:54px}
  .hero-copy p{font-size:18.5px;font-weight:700;line-height:30px;margin-top:4px}
  .btn-outline{left:520px;top:321px;width:160px;height:43px;border:2px solid var(--white);border-radius:22px;color:var(--white);font-size:15px;font-weight:600;display:flex;align-items:center;justify-content:center}

  /* Lavender band */
  .band{left:0;top:538px;width:1200px;height:555px;background:var(--lavender)}
  .feature-photo{left:235px;top:416px;width:607px;height:362px;background:linear-gradient(120deg,#9fa6ad 0%,#d9dcdf 45%,#7a7069 75%,#3a3230 100%)}
  .feature-card{left:611px;top:463px;width:356px;height:268px;background:var(--white);padding:52px 44px 0}
  .eyebrow{font-size:10.5px;font-weight:700;text-transform:uppercase}
  .feature-card h2{font-size:25.5px;font-weight:600;line-height:30px;margin-top:10px}
  .btn-solid{display:inline-flex;align-items:center;justify-content:center;width:155px;height:37px;background:var(--purple);color:var(--white);font-size:12px;font-weight:700;margin-top:22px}
  .tiles{left:235px;top:822px;display:flex;gap:19px}
  .tile{width:232px;height:205px;color:var(--white);padding:26px 20px 0}
  .tile h3{font-size:11.3px;font-weight:700;line-height:16px}
  .tile p{font-size:10.3px;line-height:16.2px;margin-top:11px;padding-left:2px}
  .tile.purple{background:var(--purple)} .tile.coral{background:var(--coral)} .tile.slate{background:var(--slate)}

  /* Work */
  .section-title{left:0;top:1149px;width:1200px;text-align:center;font-size:20.5px;font-weight:700}
  .work-photo{left:235px;top:1217px;width:357px;height:356px;background:linear-gradient(135deg,#cfd8df 0%,#f2f4f6 45%,#a8c2db 100%)}
  .work-lead{left:254px;top:1431px;width:319px;height:216px;background:var(--purple);color:var(--white);padding:26px 26px 0}
  .work-lead .eyebrow{font-size:8.5px}
  .work-lead h3{font-size:25.5px;font-weight:600;line-height:30px;margin-top:8px}
  .work-card{width:169px;height:206px;background:var(--coral);color:var(--white)}
  .work-card .thumb{height:93px}
  .work-card .body{padding:10px 15px 0}
  .work-card .eyebrow{font-size:8px}
  .work-card h4{font-size:12.5px;font-weight:700;line-height:15.5px;margin-top:6px}
  .btn-frame{left:514px;top:1698px;width:172px;height:46px;border:2px solid var(--ink);display:flex;align-items:center;justify-content:center;font-size:13px;font-weight:700}

  /* Explore */
  .explore{top:1815px;width:600px;height:437px;color:var(--white)}
  .explore.focus{left:0;background:var(--purple-deep)}
  .explore.services{left:600px;background:var(--coral)}
  .explore h2{position:absolute;top:60px;font-size:20.5px;font-weight:700;letter-spacing:.2px}
  .explore .rule{position:absolute;top:97px;width:44px;height:2px;background:var(--white)}
  .explore ul{position:absolute;top:132px;font-size:13px;font-weight:700}
  .explore li{height:30px;display:flex;align-items:center;gap:10px}
  .explore li::before{content:"›";font-size:11px;width:8px;text-align:center}
  .focus h2,.focus .rule,.focus ul{left:235px}
  .services h2,.services .rule,.services ul{left:53px}

  /* Footer */
  .footer{left:0;top:2252px;width:1200px;height:326px;background:var(--footer);color:var(--white)}
  .newsletter-lead{left:0;top:41px;width:1200px;display:flex;justify-content:center;align-items:center;gap:12px;font-size:14px;font-weight:700}
  .signup{left:434px;top:87px;width:333px;height:42px;background:var(--white);border-radius:21px;border:2px solid var(--white)}
  .signup .field{position:absolute;left:22px;top:12px;font-size:10px;color:#444}
  .signup .go{position:absolute;right:2px;top:2px;width:98px;height:34px;border-radius:17px;background:var(--purple);color:var(--white);font-size:10px;font-weight:700;display:flex;align-items:center;justify-content:center}
  .footer-rule{left:235px;top:168px;width:732px;height:1px;background:var(--footer-line)}
  .col-divider{top:168px;width:1px;height:158px;background:var(--footer-line)}
  .footer h5{font-size:11px;font-weight:700;text-transform:uppercase}
  .quick{left:235px;top:196px}
  .quick ul{position:absolute;top:34px;font-size:9px;color:var(--muted)}
  .quick li{height:19px;display:flex;gap:8px}
  .quick li::before{content:"";width:3px;height:3px;background:var(--muted);margin-top:5px}
  .question{left:568px;top:196px;font-size:10px}
  .question .label{color:var(--coral);font-weight:700;margin-top:12px}
  .question .value{color:var(--muted);margin-top:1px}
  .follow{left:798px;top:196px}
  .follow .icons{display:flex;gap:4px;margin-top:24px}
  .follow .icons i{width:22px;height:22px;background:#3b3e42;display:block}
  .base{left:0;top:2578px;width:1200px;height:47px;background:var(--footer-base);color:var(--muted);font-size:8.5px;display:flex;align-items:center;justify-content:center}
</style>
</head>
<body>

<header class="abs hero" role="img" aria-label="Blue background photo of a glowing network globe"></header>
<div class="abs topbar">
  <div class="abs contact">
    <span><svg width="12" height="12" viewBox="0 0 24 24"><path fill="#fff" d="M6.6 10.8a15.1 15.1 0 0 0 6.6 6.6l2.2-2.2c.3-.3.7-.4 1-.2 1.1.4 2.3.6 3.6.6.6 0 1 .4 1 1V20c0 .6-.4 1-1 1A17 17 0 0 1 3 4c0-.6.4-1 1-1h3.5c.6 0 1 .4 1 1 0 1.3.2 2.5.6 3.6.1.3 0 .7-.2 1z"/></svg>+000 555 0147</span>
    <span><svg width="13" height="10" viewBox="0 0 26 20"><rect width="26" height="20" rx="2" fill="#fff"/><path d="M1 2l12 9 12-9" stroke="#2a3a4c" stroke-width="2" fill="none"/></svg>hello@kelvo.org</span>
  </div>
  <div class="abs socials" aria-label="Social profiles"><i></i><i></i><i></i><i></i></div>
</div>
<div class="abs brand"><span>Kelvo</span><span class="mark"></span></div>
<nav class="abs nav"><span>HOME</span><span>ABOUT US</span><span>SERVICES</span><span>INSIGHTS</span><span>CONTACT</span></nav>
<div class="abs hero-copy">
  <h1>THINK TANKS &amp; NON-PROFITS</h1>
  <p>We have over 15 year experience in business consulting arena.<br>Learn more about our work!</p>
</div>
<a class="abs btn-outline">Get In Touch</a>

<section class="abs band"></section>
<div class="abs feature-photo" role="img" aria-label="Photo of a hand holding a pen over documents beside a laptop"></div>
<article class="abs feature-card">
  <div class="eyebrow">Nonprofits</div>
  <h2>Lorem ipsum dolor sit amet, consectetur adipiscing elit.</h2>
  <a class="btn-solid">View Case Study</a>
</article>
<div class="abs tiles">
  <div class="tile purple"><h3>Lorem ipsum dolor sit amet, con-sectetur adipiscing elit. Sed massa nunc, sagittis consectetur.</h3><p>Praesent augue leo, imperdiet in ex in, vestibulum vestibulum urna. Donec mo-lestie tortor vitae elit porta pellentesque. Nam volutpat diam eu luctus iaculis. Curabitur elementum tellus id tortor pretium ornare vitae vitae ligula.</p></div>
  <div class="tile coral"><h3>Lorem ipsum dolor sit amet, con-sectetur adipiscing elit. Sed massa nunc, sagittis consectetur.</h3><p>Praesent augue leo, imperdiet in ex in, vestibulum vestibulum urna. Donec mo-lestie tortor vitae elit porta pellentesque. Nam volutpat diam eu luctus iaculis. Curabitur elementum tellus id tortor pretium ornare vitae vitae ligula.</p></div>
  <div class="tile slate"><h3>Lorem ipsum dolor sit amet, con-sectetur adipiscing elit. Sed massa nunc, sagittis consectetur.</h3><p>Praesent augue leo, imperdiet in ex in, vestibulum vestibulum urna. Donec mo-lestie tortor vitae elit porta pellentesque. Nam volutpat diam eu luctus iaculis. Curabitur elementum tellus id tortor pretium ornare vitae vitae ligula.</p></div>
</div>

<h2 class="abs section-title">OUR WORK</h2>
<div class="abs work-photo" role="img" aria-label="Photo of hands counting banknotes over a chart"></div>
<article class="abs work-lead"><div class="eyebrow">Non-Profits</div><h3>Lorem ipsum dolor sit amet, consectetur adipiscing elit</h3></article>
<article class="abs work-card" style="left:611px;top:1217px"><div class="thumb" role="img" aria-label="Portrait photo of a smiling man" style="background:linear-gradient(160deg,#e9e9e9,#b49a86)"></div><div class="body"><div class="eyebrow">Think Tanks</div><h4>Lorem ipsum dolor sit amet, consectetur adipiscing elit</h4></div></article>
<article class="abs work-card" style="left:798px;top:1217px"><div class="thumb" role="img" aria-label="Photo of a man working in an office" style="background:linear-gradient(160deg,#dfe5ea,#8fa5b8)"></div><div class="body"><div class="eyebrow">Non-Profits</div><h4>Lorem ipsum dolor sit amet, consectetur adipiscing elit</h4></div></article>
<article class="abs work-card" style="left:611px;top:1441px"><div class="thumb" role="img" aria-label="Photo of people working on a laptop" style="background:linear-gradient(160deg,#6e7f93,#2e3440)"></div><div class="body"><div class="eyebrow">Non-Profits</div><h4>Lorem ipsum dolor sit amet, consectetur adipiscing elit</h4></div></article>
<article class="abs work-card" style="left:798px;top:1441px"><div class="thumb" role="img" aria-label="Photo of a hand on a tablet showing charts" style="background:linear-gradient(160deg,#7fa7d3,#e8d3c6)"></div><div class="body"><div class="eyebrow">Think Tanks</div><h4>Lorem ipsum dolor sit amet, consectetur adipiscing elit</h4></div></article>
<a class="abs btn-frame">View All Case Studies</a>

<section class="abs explore focus">
  <h2>EXPLORE OUR FOCUS AREAS</h2><div class="rule"></div>
  <ul>
    <li>Climate &amp; Environment Nonprofits</li>
    <li>Education Nonprofits &amp; Universities</li>
    <li>Healthcare &amp; Social Services Nonprofits</li>
    <li>Philanthropy &amp; Nonprofit Foundations</li>
    <li>Public Interest &amp; Social Justice Nonprofits</li>
    <li>Science &amp; Research Nonprofits</li>
    <li>Social Justice &amp; Community Nonprofits</li>
    <li>Think Tanks &amp; Policy Advocacy Nonprofits</li>
  </ul>
</section>
<section class="abs explore services">
  <h2>EXPLORE OUR SERVICES</h2><div class="rule"></div>
  <ul>
    <li>Brand Strategy &amp; Branding</li>
    <li>Design &amp; Design Systems</li>
    <li>Digital Strategy &amp; Web Design</li>
    <li>Content Strategy &amp; Development</li>
    <li>Strategic Consulting</li>
    <li>Workshops &amp; Training</li>
  </ul>
</section>

<footer class="abs footer">
  <div class="abs newsletter-lead"><svg width="20" height="26" viewBox="0 0 20 26"><path d="M1 1h12l6 6v18H1z" fill="none" stroke="#fff" stroke-width="1.6"/><path d="M13 1v6h6" fill="none" stroke="#fff" stroke-width="1.6"/></svg>Keep up to date — get updates with latest topics.</div>
  <div class="abs signup"><span class="field">your email address</span><span class="go">SIGN ME UP!</span></div>
  <div class="abs footer-rule"></div>
  <div class="abs col-divider" style="left:498px"></div>
  <div class="abs col-divider" style="left:733px"></div>
  <div class="abs quick">
    <h5>Quick Links</h5>
    <ul style="left:0"><li>Home</li><li>About Us</li><li>Services</li></ul>
    <ul style="left:140px"><li>Insights</li><li>Contact us</li></ul>
  </div>
  <div class="abs question">
    <h5>You've Question?</h5>
    <div class="label">Get a Quote</div><div class="value">(000) 555-0147</div>
    <div class="label">Send Email</div><div class="value">hello@kelvo.org</div>
  </div>
  <div class="abs follow">
    <h5>Follow Us</h5>
    <div class="icons" aria-label="Social profiles"><i></i><i></i><i></i><i></i></div>
  </div>
</footer>
<div class="abs base">Copyright © 2020 Kelvo.&nbsp; All rights reserved.</div>

</body>
</html>
```